Breakfast Briefings / Lunch & Learn

I would like to have a double sided flyer size 8x10 to display the breakfast briefing on one side and Lunch & Learn on the other side.

Header on each side to say
2018 Calendar Breakfast Briefing (on the breakfast side)
2018 Calendar Lunch & Learn (on the lunch side)

I have attached a copy of the files we would like to use.

Industry/Entity Type

Learn

Colors

Designer to choose colors to be used in the design.

```html
<!DOCTYPE html>
<html lang="en">
<head>
<meta charset="utf-8">
<title>2018 Calendar Lunch &amp; Learn</title>
<link href="https://fonts.googleapis.com/css2?family=Jost:wght@400;500;700&display=swap" rel="stylesheet">
<style>
  :root {
    --sky: #a8c8e7;
    --sky-deep: #7fb2df;
    --ring-light: #5aa6dc;
    --ring-mid: #3d8fcd;
    --navy-blue: #1a70ae;
    --badge-blue: #1f7fc2;
    --white: #ffffff;
    --ink: #0e2740;
    --brand-grey: #4a4f55;
  }
  html, body {
    margin: 0;
    padding: 0;
    overflow: hidden;
  }
  .flyer {
    position: relative;
    width: 960px;
    height: 1200px;
    background: var(--sky);
    overflow: hidden;
    font-family: "Jost", "Futura", sans-serif;
  }
  .flyer__shapes {
    position: absolute;
    inset: 0;
  }
  .header {
    position: absolute;
    left: 62px;
    top: 40px;
    color: var(--white);
  }
  .header__year {
    position: absolute;
    left: 0;
    top: 232px;
    transform: rotate(-90deg);
    transform-origin: left top;
    font-size: 76px;
    font-weight: 700;
    letter-spacing: 2px;
    line-height: 1;
  }
  .header__divider-v {
    position: absolute;
    left: 88px;
    top: 4px;
    width: 3px;
    height: 228px;
    background: var(--white);
  }
  .header__divider-h {
    position: absolute;
    left: 88px;
    top: 58px;
    width: 322px;
    height: 2px;
    background: var(--white);
  }
  .header__kicker {
    position: absolute;
    left: 98px;
    top: -4px;
    font-size: 48px;
    font-weight: 700;
    line-height: 1.2;
    white-space: nowrap;
  }
  .header__title {
    position: absolute;
    left: 96px;
    top: 54px;
    font-size: 84px;
    font-weight: 700;
    line-height: 0.98;
    white-space: nowrap;
  }
  .badge-label {
    font-family: "Jost", "Futura", sans-serif;
    font-weight: 700;
    font-size: 31px;
    fill: var(--white);
  }
  .schedule {
    position: absolute;
    left: 107px;
    top: 578px;
    margin: 0;
    padding: 0;
    list-style: none;
    color: var(--ink);
    font-size: 22.5px;
    line-height: 1.25;
  }
  .schedule__item {
    margin-bottom: 17px;
  }
  .schedule__month {
    font-weight: 500;
  }
  .schedule__note {
    display: block;
    padding-left: 143px;
  }
  .brand {
    position: absolute;
    left: 700px;
    top: 1050px;
    display: flex;
    align-items: center;
    gap: 14px;
    color: var(--brand-grey);
    font-size: 50px;
    font-weight: 500;
    letter-spacing: 3px;
    line-height: 1;
  }
  .brand__dot {
    width: 26px;
    height: 26px;
    border-radius: 50%;
    background: var(--badge-blue);
  }
</style>
</head>
<body>
<main class="flyer">
  <svg class="flyer__shapes" width="960" height="1200" viewBox="0 0 960 1200" aria-hidden="true">
    <defs>
      <filter id="soft-shadow" x="-20%" y="-20%" width="140%" height="140%">
        <feDropShadow dx="0" dy="4" stdDeviation="6" flood-color="#2b5a85" flood-opacity="0.35"/>
      </filter>
    </defs>

    <!-- header disc -->
    <g class="header-disc">
      <circle cx="183" cy="-20" r="478" fill="var(--white)" filter="url(#soft-shadow)"/>
      <circle cx="183" cy="-20" r="440" fill="var(--ring-light)"/>
      <circle cx="183" cy="-20" r="420" fill="var(--ring-mid)"/>
      <circle cx="183" cy="-20" r="398" fill="var(--navy-blue)"/>
    </g>

    <!-- life long learn disc -->
    <g class="theme-disc">
      <circle cx="935" cy="515" r="200" fill="var(--sky-deep)"/>
      <circle cx="935" cy="515" r="185" fill="var(--white)" filter="url(#soft-shadow)"/>
      <circle cx="935" cy="515" r="168" fill="var(--navy-blue)"/>
      <circle cx="985" cy="515" r="128" fill="none" stroke="var(--ring-light)" stroke-width="2"/>
    </g>

    <g class="theme-badges">
      <circle cx="813" cy="366" r="58" fill="var(--white)" filter="url(#soft-shadow)"/>
      <circle cx="813" cy="366" r="52" fill="var(--badge-blue)"/>
      <text class="badge-label" x="813" y="377" text-anchor="middle">Life</text>

      <circle cx="770" cy="523" r="58" fill="var(--white)" filter="url(#soft-shadow)"/>
      <circle cx="770" cy="523" r="52" fill="var(--badge-blue)"/>
      <text class="badge-label" x="770" y="534" text-anchor="middle">Long</text>

      <circle cx="853" cy="660" r="58" fill="var(--white)" filter="url(#soft-shadow)"/>
      <circle cx="853" cy="660" r="52" fill="var(--badge-blue)"/>
      <text class="badge-label" x="853" y="671" text-anchor="middle">Learn</text>
    </g>

    <!-- brand disc -->
    <g class="brand-disc">
      <circle cx="905" cy="1075" r="258" fill="var(--sky-deep)"/>
      <circle cx="905" cy="1075" r="228" fill="var(--white)" filter="url(#soft-shadow)"/>
    </g>
  </svg>

  <header class="header">
    <div class="header__year">2018</div>
    <div class="header__divider-v"></div>
    <div class="header__divider-h"></div>
    <div class="header__kicker">Calendar</div>
    <h1 class="header__title" style="margin:0">Lunch<br>&amp; Learn</h1>
  </header>

  <ul class="schedule">
    <li class="schedule__item"><span class="schedule__month">March:</span> Mindfulness</li>
    <li class="schedule__item"><span class="schedule__month">April:</span> Nutrition and Lifestyle Coaching</li>
    <li class="schedule__item"><span class="schedule__month">May:</span> What is Neuromodulation?</li>
    <li class="schedule__item"><span class="schedule__month">June:</span> Achieve Your Goals</li>
    <li class="schedule__item"><span class="schedule__month">July:</span> Changing Your Life with Positive Thinking</li>
    <li class="schedule__item"><span class="schedule__month">August:</span> What is Clean Eating and How Do I Get Started?</li>
    <li class="schedule__item"><span class="schedule__month">September:</span> Budgeting 101 Financial Wellness</li>
    <li class="schedule__item"><span class="schedule__month">October:</span> Busted! Nutritional Myths</li>
    <li class="schedule__item"><span class="schedule__month">November:</span> Time Management:<span class="schedule__note">- No Time Like The Present</span></li>
    <li class="schedule__item"><span class="schedule__month">December:</span> 1st Time Home Buyers</li>
  </ul>

  <div class="brand">
    <span class="brand__dot"></span>
    <span class="brand__name">lumeno</span>
  </div>
</main>
</body>
</html>
```